Website design: professional but personally
Needs:
Our visitors are mostly people that look for a IT or technical jobs, but our customers are also visiting our website.
Core values are: personally, professional, ambition, growth, personal development
Terms that we think of are:
Professional, but personal (we ware no trading company, but we do have internation customers)
People
IT (jobs)
Engineering (jobs)

```html
<!DOCTYPE html>
<html lang="nl">
<head>
<meta charset="utf-8">
<title>Talvora – Talent Solutions</title>
<link rel="stylesheet" href="https://fonts.googleapis.com/css2?family=Open+Sans:wght@400;600;700&family=Ubuntu:wght@500;700&display=swap">
<style>
:root{
  --green:#8cc63f;
  --dark:#2b2b2b;
  --ink:#3a3a3a;
  --muted:#666;
  --white:#fff;
  --line:#e6e6e6;
  --mapbg:#e9ebec;
}
*{box-sizing:border-box;margin:0;padding:0}
html,body{width:1200px;height:3686px;overflow:hidden;background:var(--white)}
body{position:relative;font-family:"Open Sans",Arial,sans-serif;color:var(--ink)}
.abs{position:absolute}
.section{position:absolute;left:0;width:1200px;overflow:hidden}
.heading{font-family:"Ubuntu","Open Sans",sans-serif;font-weight:700}

/* hero */
.hero{top:0;height:706px}
.hero-photo{position:absolute;inset:0;background:linear-gradient(100deg,#6f6d6a 0%,#b9b5b0 35%,#d8d4cf 60%,#8d8a86 100%)}
.hero-shade{position:absolute;inset:0;background:linear-gradient(180deg,rgba(0,0,0,.25),rgba(0,0,0,.05) 30%,rgba(255,255,255,.1))}
.brand{left:100px;top:14px;color:var(--white);font-family:"Ubuntu",sans-serif;font-weight:700;font-size:30px;letter-spacing:2px}
.menu{left:1068px;top:14px}
.hero-title{left:0;width:1180px;top:292px;text-align:center;color:var(--green);font-size:42px}
.hero-text{left:0;width:1180px;top:340px;text-align:center;color:var(--white);font-size:25px;line-height:32px}

/* job choice */
.jobs{top:706px;height:410px;background:var(--white)}
.jobs-photo{left:0;top:0;width:660px;height:410px;background:linear-gradient(90deg,#f3f0ec,#e2dcd5 40%,#ffffff)}
.job-circle{width:202px;height:202px;border-radius:50%;display:flex;flex-direction:column;align-items:center;justify-content:center;text-align:center}
.job-circle strong{font-family:"Ubuntu",sans-serif;font-size:22px;font-weight:700}
.job-circle span{font-size:10px;font-weight:700;letter-spacing:.3px}
.job-it{left:662px;top:94px;background:var(--green);color:var(--dark)}
.job-eng{left:884px;top:94px;background:var(--dark);color:var(--white)}

/* success factors */
.factors{top:1116px;height:440px;background:var(--white)}
.eyebrow{color:var(--green);font-size:20px;font-weight:700}
.factors .eyebrow{left:100px;top:88px}
.factors-title{left:100px;top:122px;width:520px;font-size:22px;line-height:30px;color:var(--ink);text-transform:uppercase}
.factors-text{left:100px;top:224px;width:500px;font-size:17px;line-height:30px;color:var(--muted);text-align:justify}
.factors-photo{left:640px;top:46px;width:460px;height:394px;background:linear-gradient(180deg,#ece8e3,#c9c3bd 60%,#dedad6)}

/* business solutions */
.business{top:1556px;height:480px}
.business-photo{position:absolute;inset:0;background:linear-gradient(110deg,#2d2a27,#4a4440 40%,#3a3532 65%,#6b6660)}
.business-title{left:0;width:1180px;top:150px;text-align:center;color:var(--white);font-size:50px;letter-spacing:1px}
.business-rule{left:488px;top:218px;width:222px;height:4px;background:var(--green)}
.business-text{left:180px;width:840px;top:236px;text-align:center;color:var(--white);font-size:15px;line-height:22px}
.arrow{top:190px}

/* usp */
.usp{top:2036px;height:464px;background:var(--white)}
.usp-title{left:0;width:1200px;top:70px;text-align:center;color:var(--green);font-size:25px}
.usp-card{top:144px;width:238px;height:232px;text-align:center}
.usp-card.is-active{border:2px solid var(--line)}
.usp-icon{display:block;margin:34px auto 0}
.usp-card p{margin-top:24px;font-size:15px;line-height:22px;color:var(--muted)}

/* customers */
.customers{top:2500px;height:466px}
.customers-photo{position:absolute;inset:0;background:linear-gradient(180deg,#3e3e3e,#5c5c5c 55%,#2f2f2f)}
.customers-title{left:0;width:1200px;top:28px;text-align:center;color:var(--green);font-size:28px}
.testimonial{top:90px;width:330px;text-align:center;color:var(--white)}
.avatar{width:156px;height:156px;margin:0 auto;border-radius:50%;border:4px solid var(--white);background:linear-gradient(180deg,#d9d4cf,#9c958f)}
.testimonial h3{font-weight:400;font-size:19px;margin-top:16px}
.quote{position:relative;margin:10px auto 0;width:240px;font-size:15px;line-height:22px}
.quote .q{position:absolute;font-family:Georgia,serif;font-size:44px;font-weight:700;line-height:1}
.quote .open{left:-30px;top:-4px}
.quote .close{right:-32px;bottom:-20px}
.btn{left:536px;top:418px;width:112px;height:30px;background:var(--green);color:var(--dark);font-size:14px;font-weight:700;display:flex;align-items:center;justify-content:center;border:1px solid #6e9f2e}

/* coverage */
.coverage{top:2966px;height:420px}
.map{position:absolute;inset:0;background:linear-gradient(90deg,#d5d8da,var(--mapbg) 40%,#dfe2e3)}
.coverage-box{left:680px;top:110px;width:420px;height:204px;background:var(--green);color:var(--white);display:flex;align-items:center;justify-content:center;text-align:center;font-family:"Ubuntu",sans-serif;font-weight:700;font-size:16px;line-height:22px;text-transform:uppercase}

/* footer */
.footer{top:3386px;height:300px;background:var(--white)}
.footer-col{top:54px}
.footer-col h4{color:var(--green);font-size:14px;font-weight:700;text-transform:uppercase;margin-bottom:22px}
.footer-col li{list-style:none;font-size:15px;line-height:30px;color:var(--muted)}
.social li{display:flex;align-items:center;gap:14px}
.social .dot{width:14px;height:14px;border-radius:50%;background:var(--dark)}
.footer-base{left:0;top:290px;width:1200px;height:10px;background:#eee}
</style>
</head>
<body>

<section class="section hero">
  <div class="hero-photo" role="img" aria-label="Smiling professional woman working on a laptop in a bright office"></div>
  <div class="hero-shade"></div>
  <div class="abs brand">Talvora</div>
  <svg class="abs menu" width="36" height="32" viewBox="0 0 36 32"><rect y="3" width="34" height="5" rx="2" fill="#fff"/><rect y="13" width="34" height="5" rx="2" fill="#fff"/><rect y="23" width="34" height="5" rx="2" fill="#fff"/></svg>
  <h1 class="abs heading hero-title">TALENT SOLUTIONS</h1>
  <p class="abs hero-text">richt zich volledig op de sourcing en het ontwikkelen<br>van hoogopgeleid IT en technisch talent.</p>
</section>

<section class="section jobs">
  <div class="abs jobs-photo" role="img" aria-label="Young businessman in a white shirt and tie gesturing towards the job options"></div>
  <a class="abs job-circle job-it"><strong>IT</strong><span>(TECHNICAL) JOBS</span></a>
  <a class="abs job-circle job-eng"><strong>ENGINEERING</strong><span>(TECHNICAL) JOBS</span></a>
</section>

<section class="section factors">
  <p class="abs eyebrow">ONZE SUCCESFACTOREN</p>
  <h2 class="abs heading factors-title">1000+ IT en technische professionals in vaste dienst</h2>
  <p class="abs factors-text">Als enige organisatie in Nederland heeft Talvora ruim 1000 jonge ICT en technische medewerkers voor u klaar staan. Talvora is een betrouwbare installatiepartner voor de groot zakelijke markt.</p>
  <div class="abs factors-photo" role="img" aria-label="Smiling young professional in a suit holding a tablet"></div>
</section>

<section class="section business">
  <div class="business-photo" role="img" aria-label="Professional working on a laptop in a dim office"></div>
  <h2 class="abs heading business-title">BUSINESS SOLUTIONS</h2>
  <div class="abs business-rule"></div>
  <p class="abs business-text">Optimale ondersteuning van uw primaire bedrijfsprocessen? Wij ontzorgen support afdelingen op operationeel gebied: van individueel niveau tot het compleet outsourcen. Business Solutions richt zich hoofdzakelijk op de ontwikkeling en het detacheren van 1e, 2e en 3e lijn Support Engineers.</p>
  <svg class="abs arrow" style="left:58px" width="44" height="76" viewBox="0 0 44 76"><polyline points="40,4 6,38 40,72" fill="none" stroke="#8cc63f" stroke-width="5"/></svg>
  <svg class="abs arrow" style="left:1098px" width="44" height="76" viewBox="0 0 44 76"><polyline points="4,4 38,38 4,72" fill="none" stroke="#8cc63f" stroke-width="5"/></svg>
</section>

<section class="section usp">
  <h2 class="abs heading usp-title">SUCCESVOL OMDAT WE HET ANDERS DOEN</h2>
  <div class="abs usp-card is-active" style="left:98px">
    <svg class="usp-icon" width="100" height="100" viewBox="0 0 100 100"><circle cx="50" cy="50" r="50" fill="#8cc63f"/><circle cx="45" cy="44" r="15" fill="none" stroke="#fff" stroke-width="4"/><line x1="56" y1="55" x2="70" y2="69" stroke="#fff" stroke-width="6" stroke-linecap="round"/></svg>
    <p>Uzersterk in de werving<br>van young professionals</p>
  </div>
  <div class="abs usp-card" style="left:352px">
    <svg class="usp-icon" width="100" height="100" viewBox="0 0 100 100"><circle cx="50" cy="50" r="50" fill="#8cc63f"/><polygon points="50,24 57,42 76,42 61,54 67,73 50,62 33,73 39,54 24,42 43,42" fill="none" stroke="#fff" stroke-width="3" stroke-linejoin="round"/></svg>
    <p>Uzersterk in de werving<br>van young professionals</p>
  </div>
  <div class="abs usp-card" style="left:606px">
    <svg class="usp-icon" width="100" height="100" viewBox="0 0 100 100"><circle cx="50" cy="50" r="50" fill="#8cc63f"/><path d="M28 46a22 22 0 0 1 40-12" fill="none" stroke="#fff" stroke-width="3"/><polyline points="70,24 69,35 58,34" fill="none" stroke="#fff" stroke-width="3"/><path d="M72 54a22 22 0 0 1-40 12" fill="none" stroke="#fff" stroke-width="3"/><polyline points="30,76 31,65 42,66" fill="none" stroke="#fff" stroke-width="3"/></svg>
    <p>Uzersterk in de werving<br>van young professionals</p>
  </div>
  <div class="abs usp-card" style="left:860px">
    <svg class="usp-icon" width="100" height="100" viewBox="0 0 100 100"><circle cx="50" cy="50" r="50" fill="#8cc63f"/><path d="M34 24h24l10 10v42H34z" fill="none" stroke="#fff" stroke-width="3" stroke-linejoin="round"/><path d="M58 36a9 9 0 1 0 0 16" fill="none" stroke="#fff" stroke-width="3"/><line x1="42" y1="42" x2="54" y2="42" stroke="#fff" stroke-width="2.5"/><line x1="42" y1="47" x2="54" y2="47" stroke="#fff" stroke-width="2.5"/></svg>
    <p>Uzersterk in de werving<br>van young professionals</p>
  </div>
</section>

<section class="section customers">
  <div class="customers-photo" role="img" aria-label="Dark city skyline behind the customer testimonials"></div>
  <h2 class="abs heading customers-title">OUR CUSTOMERS</h2>
  <div class="abs testimonial" style="left:106px">
    <div class="avatar" role="img" aria-label="Portrait of customer Candressa"></div>
    <h3>Candressa</h3>
    <p class="quote"><span class="q open">“</span>Optimale ondersteuning van uw primaire bedrijfsprocessen? Wij ontzorgen support afdelingen op operationeel gebied<span class="q close">”</span></p>
  </div>
  <div class="abs testimonial" style="left:438px">
    <div class="avatar" role="img" aria-label="Portrait of customer Tonkin"></div>
    <h3>Tonkin</h3>
    <p class="quote"><span class="q open">“</span>Optimale ondersteuning van uw primaire bedrijfsprocessen? Wij ontzorgen support afdelingen op operationeel gebied<span class="q close">”</span></p>
  </div>
  <div class="abs testimonial" style="left:770px">
    <div class="avatar" role="img" aria-label="Portrait of customer George"></div>
    <h3>George</h3>
    <p class="quote"><span class="q open">“</span>Optimale ondersteuning van uw primaire bedrijfsprocessen? Wij ontzorgen support afdelingen op operationeel gebied<span class="q close">”</span></p>
  </div>
  <a class="abs btn">VIEW MORE</a>
</section>

<section class="section coverage">
  <div class="map" role="img" aria-label="Map of the Netherlands with markers for employee locations across the country"></div>
  <div class="abs coverage-box">Onze medewerkers zijn door<br>heel Nederland inzetbaar.<br>We hebben een landelijk<br>dekkend personeelsbestand.</div>
</section>

<footer class="section footer">
  <div class="abs footer-col" style="left:106px">
    <h4>Adresgegevens</h4>
    <ul><li>Talvora B.V.</li><li>Lindelaan 218B</li><li>3512 KT Utrecht</li><li>0850 123 456</li><li>Privacy Policy</li></ul>
  </div>
  <div class="abs footer-col" style="left:358px">
    <h4>Voor opdrachtgevers</h4>
    <ul><li>Klanten over Talvora</li><li>Login urenregistratiesysteem</li><li>Nieuws</li></ul>
  </div>
  <div class="abs footer-col" style="left:648px">
    <h4>Voor werkzoekenden</h4>
    <ul><li>IT Traineeship</li><li>Technisch Traineeship</li><li>Werken en leren in de ICT</li><li>Sollicitatietips</li></ul>
  </div>
  <div class="abs footer-col social" style="left:934px">
    <h4>Connect</h4>
    <ul><li><span class="dot"></span>Microblog</li><li><span class="dot"></span>Social</li><li><span class="dot"></span>Network</li><li><span class="dot"></span>Video</li></ul>
  </div>
  <div class="abs footer-base"></div>
</footer>

</body>
</html>
```